Become a Mentor - For Musicians, Artists, Producers and Teachers

Here is the full creative brief:

https://files.plenwick.com/sheets/d/4kTqpLm8Wz_2RNa7Hc3Xv91Jd0Gb5YeUsQ6fNo8rTpxa/view?mode=shared

Here is the background image file: https://www.trovecrate.com/sh/83jbwtrmq5dkx2u/BBHn4k7QTf2ZpLeXX-wr9MUHe?dl=0

LOGO:
https://www.trovecrate.com/sh/k472rufmpdo9b6w/BBKLe3RtHY5J-sFQnLZw7Ggma?dl=0

```html
<!DOCTYPE html>
<html lang="en">
<head>
<meta charset="utf-8">
<title>Become a Mentor Today – Meridian Academy of Sound</title>
<link rel="stylesheet" href="https://fonts.googleapis.com/css2?family=Anton&family=Lobster&family=Montserrat:wght@700;800&display=swap">
<style>
  :root {
    --brand-blue: #2f7bc0;
    --brand-blue-light: #5a95cf;
    --deep-navy: #1c4f86;
    --white: #ffffff;
    --photo-dark: #2a2420;
    --photo-mid: #6b5d52;
    --photo-warm: #a88a73;
    --photo-grey: #8d8b88;
  }
  * { margin: 0; padding: 0; box-sizing: border-box; }
  html, body { width: 905px; height: 1200px; overflow: hidden; background: var(--brand-blue); }
  .flyer {
    position: relative;
    width: 905px;
    height: 1200px;
    overflow: hidden;
    background: var(--brand-blue);
    color: var(--white);
  }
  .flyer__art { position: absolute; inset: 0; width: 905px; height: 1200px; }
  .kicker {
    position: absolute; top: 34px; left: 0; width: 100%;
    text-align: center;
    font-family: "Anton", "Impact", sans-serif;
    font-size: 46px; letter-spacing: 0.5px;
    text-shadow: 0 0 10px rgba(255,255,255,0.75), 0 0 3px rgba(255,255,255,0.6);
  }
  .headline {
    position: absolute; left: 0; width: 100%;
    text-align: center;
    font-family: "Lobster", cursive;
    font-weight: 400;
    line-height: 1;
    text-shadow: 2px 3px 0 rgba(40,40,40,0.85), 0 4px 10px rgba(0,0,0,0.35);
  }
  .headline--line1 { top: 318px; font-size: 108px; padding-left: 20px; }
  .headline--line2 { top: 410px; font-size: 118px; }
  .subline {
    position: absolute; top: 556px; left: 0; width: 100%;
    text-align: center;
    font-family: "Anton", "Impact", sans-serif;
    font-size: 28px;
    text-shadow: 1px 2px 2px rgba(0,0,0,0.8);
  }
  .brand {
    position: absolute; top: 800px; left: 0; width: 100%;
    display: flex; align-items: center; justify-content: center; gap: 14px;
  }
  .brand__dot {
    width: 46px; height: 46px; border-radius: 50%;
    background: var(--white);
  }
  .brand__name {
    font-family: "Anton", "Impact", sans-serif;
    font-size: 40px; letter-spacing: 1px;
    color: var(--white);
  }
  .audience {
    position: absolute; top: 930px; left: 0; width: 100%;
    text-align: center;
    font-family: "Anton", "Impact", sans-serif;
    font-size: 36px;
  }
  .cta {
    position: absolute; top: 992px; left: 168px;
    width: 568px; height: 62px;
    background: var(--white);
    display: flex; align-items: center; justify-content: center;
  }
  .cta__label {
    font-family: "Lobster", cursive;
    font-size: 44px;
    color: var(--deep-navy);
  }
  .phone {
    position: absolute; top: 1058px; left: 0; width: 100%;
    display: flex; align-items: center; justify-content: center; gap: 22px;
  }
  .phone__icon { width: 44px; height: 48px; }
  .phone__number {
    font-family: "Anton", "Impact", sans-serif;
    font-size: 80px; line-height: 1; letter-spacing: 1px;
  }
  .web {
    position: absolute; top: 1140px; left: 0; width: 100%;
    display: flex; align-items: center; justify-content: center; gap: 8px;
  }
  .web__icon { width: 28px; height: 28px; }
  .web__address {
    font-family: "Montserrat", sans-serif;
    font-weight: 800;
    font-size: 20px; letter-spacing: 0.3px;
  }
</style>
</head>
<body>
<main class="flyer">
  <svg class="flyer__art" viewBox="0 0 905 1200" role="img" aria-label="Photograph of two young musicians talking in a recording studio beside a mixing desk and speaker">
    <defs>
      <linearGradient id="studio-photo" x1="0" y1="0" x2="1" y2="1">
        <stop offset="0" stop-color="var(--photo-warm)"/>
        <stop offset="0.35" stop-color="var(--photo-grey)"/>
        <stop offset="0.65" stop-color="var(--photo-mid)"/>
        <stop offset="1" stop-color="var(--photo-dark)"/>
      </linearGradient>
    </defs>
    <polygon class="photo-area" points="0,0 905,0 905,596 453,768 0,596" fill="url(#studio-photo)"/>
    <polygon class="photo-veil" points="0,575 453,745 905,575 905,610 453,768 0,610" fill="var(--brand-blue-light)" opacity="0.55"/>
  </svg>
  <svg class="flyer__art" viewBox="0 0 905 1200" aria-hidden="true">
    <polygon class="top-chevron" points="0,0 905,0 905,12 453,146 0,12" fill="var(--brand-blue)"/>
  </svg>

  <h2 class="kicker">Start Your Career</h2>
  <h1>
    <span class="headline headline--line1">Become a</span>
    <span class="headline headline--line2">Mentor Today</span>
  </h1>
  <p class="subline">Turn your skills and passion for music into a career</p>

  <div class="brand">
    <span class="brand__dot"></span>
    <span class="brand__name">MERIDIAN ACADEMY OF SOUND</span>
  </div>

  <p class="audience">Designed for Musicians, Artists, Producers &amp; Teachers</p>

  <div class="cta"><span class="cta__label">Apply Now!</span></div>

  <div class="phone">
    <svg class="phone__icon" viewBox="0 0 24 26" aria-hidden="true">
      <path d="M6 1c1.2-.6 2.2 0 2.7 1.2l1.6 3.8c.4 1-.1 2-1 2.5l-1.5.9c1 3.4 3 6.6 5.7 8.8l1.4-1c.9-.6 2-.5 2.7.3l2.7 3.2c.8 1 .6 2.2-.4 2.9l-1.7 1.2C14 27 3.8 14.7 3.5 5.5 3.4 3.6 4.4 1.8 6 1z" fill="var(--white)"/>
    </svg>
    <span class="phone__number">1300 482 610</span>
  </div>

  <div class="web">
    <svg class="web__icon" viewBox="0 0 28 28" aria-hidden="true" fill="none" stroke="var(--white)" stroke-width="2">
      <circle cx="14" cy="14" r="12"/>
      <ellipse cx="14" cy="14" rx="5.5" ry="12"/>
      <line x1="2" y1="14" x2="26" y2="14"/>
      <path d="M4.5 7.5h19M4.5 20.5h19"/>
    </svg>
    <span class="web__address">www.meridianacademyofsound.com.au</span>
  </div>
</main>
</body>
</html>
```